Hair Salon using organic products looking for AWSOME new menu's!!

We want different and fun incorporating our logo. We would love a folding or tri-folding menu. Any ideas would be welcome we like different. We are an quilmo salon in a little colonial town, but don't like the colonial feel. we would like menu's that would not cost an arm and a leg to print. And we could update as prices and services change without having to re-do the entire design.

Target Market(s)

upper class clients with an interest in using plant based products on their hair and skin

Industry/Entity Type

Hair And Beauty

Requirements
Must have
• Logo, area for contact information and ability to list all salon services
Nice to have
• just a really fun different look to set us aside from other salons. We like to be different

```html
<!DOCTYPE html>
<html lang="en">
<head>
<meta charset="utf-8">
<title>Lumen Salon – Service Menu</title>
<link href="https://fonts.googleapis.com/css2?family=Cinzel:wght@400;600&family=Cormorant+Garamond:ital,wght@0,400;0,500;1,500&display=swap" rel="stylesheet">
<style>
  :root {
    --page: #f1f1ef;
    --ink: #0c0c0c;
    --panel-edge: #1c1c1c;
    --gold: #c9a43a;
    --gold-light: #e4c76a;
    --text: #e9e4d6;
    --muted: #8a8170;
  }
  * { box-sizing: border-box; margin: 0; padding: 0; }
  html, body { width: 900px; height: 1200px; overflow: hidden; background: var(--page); }
  body { position: relative; font-family: "Cormorant Garamond", Georgia, serif; }

  .menu-spread {
    position: absolute; left: 20px; top: 377px;
    width: 860px; height: 446px;
    background: var(--ink);
    display: grid; grid-template-columns: repeat(3, 1fr);
    box-shadow: 0 6px 18px rgba(0,0,0,.18);
  }
  .panel { position: relative; padding: 26px 30px; }
  .panel + .panel { border-left: 1px solid var(--panel-edge); }

  .menu-title {
    font-family: "Cinzel", Georgia, serif;
    color: var(--gold); text-align: center;
    font-size: 26px; letter-spacing: 3px; font-weight: 400;
    padding-bottom: 6px; margin-bottom: 14px;
    border-bottom: 1px solid var(--gold);
  }

  .service-group { margin-bottom: 16px; }
  .group-heading {
    border: 1px solid var(--gold);
    color: var(--gold-light);
    font-style: italic; font-weight: 500;
    font-size: 14px; text-align: center;
    height: 24px; line-height: 22px;
    margin-bottom: 8px;
  }
  .group-heading::before, .group-heading::after {
    content: ""; display: inline-block; width: 5px; height: 5px;
    background: var(--gold); transform: rotate(45deg);
    margin: 0 8px; vertical-align: middle;
  }
  .service-item {
    display: flex; align-items: baseline;
    color: var(--text); font-size: 11.5px; line-height: 16px;
  }
  .service-item .leader { flex: 1; border-bottom: 1px dotted var(--muted); margin: 0 6px; transform: translateY(-3px); }
  .service-item .price { color: var(--gold-light); }

  .brand-panel { display: flex; flex-direction: column; align-items: center; justify-content: center; }
  .brand-dot { width: 120px; height: 120px; border-radius: 50%; background: radial-gradient(circle at 40% 35%, var(--gold-light), var(--gold)); margin-bottom: 26px; }
  .brand-name {
    font-family: "Cinzel", Georgia, serif; color: var(--gold);
    font-size: 22px; letter-spacing: 4px; font-weight: 400;
  }
  .brand-web {
    font-family: "Cinzel", Georgia, serif; color: var(--gold);
    font-size: 11px; letter-spacing: 2px; margin-top: 4px;
  }
</style>
</head>
<body>
  <main class="menu-spread">
    <section class="panel services-left">
      <div class="service-group">
        <h3 class="group-heading">Heading</h3>
        <p class="service-item"><span>Lorem Ipsum</span><span class="leader"></span><span class="price">$ 00</span></p>
        <p class="service-item"><span>Lorem Ipsum</span><span class="leader"></span><span class="price">$ 00</span></p>
        <p class="service-item"><span>Lorem Ipsum</span><span class="leader"></span><span class="price">$ 00</span></p>
      </div>
      <div class="service-group">
        <h3 class="group-heading">Heading</h3>
        <p class="service-item"><span>Lorem Ipsum</span><span class="leader"></span><span class="price">$ 00</span></p>
        <p class="service-item"><span>Lorem Ipsum</span><span class="leader"></span><span class="price">$ 00</span></p>
        <p class="service-item"><span>Lorem Ipsum</span><span class="leader"></span><span class="price">$ 00</span></p>
        <p class="service-item"><span>Lorem Ipsum</span><span class="leader"></span><span class="price">$ 00</span></p>
      </div>
      <div class="service-group">
        <h3 class="group-heading">Heading</h3>
        <p class="service-item"><span>Lorem Ipsum</span><span class="leader"></span><span class="price">$ 00</span></p>
        <p class="service-item"><span>Lorem Ipsum</span><span class="leader"></span><span class="price">$ 00</span></p>
        <p class="service-item"><span>Lorem Ipsum</span><span class="leader"></span><span class="price">$ 00</span></p>
        <p class="service-item"><span>Lorem Ipsum</span><span class="leader"></span><span class="price">$ 00</span></p>
        <p class="service-item"><span>Lorem Ipsum</span><span class="leader"></span><span class="price">$ 00</span></p>
        <p class="service-item"><span>Lorem Ipsum</span><span class="leader"></span><span class="price">$ 00</span></p>
        <p class="service-item"><span>Lorem Ipsum</span><span class="leader"></span><span class="price">$ 00</span></p>
      </div>
    </section>

    <section class="panel services-center">
      <h1 class="menu-title">MENU</h1>
      <div class="service-group">
        <h3 class="group-heading">Heading</h3>
        <p class="service-item"><span>Lorem Ipsum</span><span class="leader"></span><span class="price">$ 00</span></p>
        <p class="service-item"><span>Lorem Ipsum</span><span class="leader"></span><span class="price">$ 00</span></p>
        <p class="service-item"><span>Lorem Ipsum</span><span class="leader"></span><span class="price">$ 00</span></p>
        <p class="service-item"><span>Lorem Ipsum</span><span class="leader"></span><span class="price">$ 00</span></p>
      </div>
      <div class="service-group">
        <h3 class="group-heading">Heading</h3>
        <p class="service-item"><span>Lorem Ipsum</span><span class="leader"></span><span class="price">$ 00</span></p>
        <p class="service-item"><span>Lorem Ipsum</span><span class="leader"></span><span class="price">$ 00</span></p>
        <p class="service-item"><span>Lorem Ipsum</span><span class="leader"></span><span class="price">$ 00</span></p>
        <p class="service-item"><span>Lorem Ipsum</span><span class="leader"></span><span class="price">$ 00</span></p>
      </div>
      <div class="service-group">
        <h3 class="group-heading">Heading</h3>
        <p class="service-item"><span>Lorem Ipsum</span><span class="leader"></span><span class="price">$ 00</span></p>
        <p class="service-item"><span>Lorem Ipsum</span><span class="leader"></span><span class="price">$ 00</span></p>
        <p class="service-item"><span>Lorem Ipsum</span><span class="leader"></span><span class="price">$ 00</span></p>
      </div>
    </section>

    <section class="panel brand-panel">
      <div class="brand-dot"></div>
      <h2 class="brand-name">LUMEN SALON</h2>
      <p class="brand-web">www.lumensalon.com</p>
    </section>
  </main>
</body>
</html>
```